Website front end design for an education nonprofit

This project involves design and development of the website front end (i.e., Web user interface and user experience design) for MOVA Sphere, a nonprofit initiative for developing an online platform for basic English language instruction, especially targeted toward underprivileged, non-native English speaking populations.

More about us: We are a team of educators, researchers and engineers passionate about this cause and would like to invite talented, creative web developers to join us in this effort to create positive social impact! Please send a personal message to the project owner for the executive summary to get more information about our initiative, big picture vision and the team.

MOVA Sphere website front end (UI/UX) design
Our key goals for this project are to develop an impressive Drupal-based front end for our website as well as to find really talented and creative web/UI/UX designers-cum-developers who are experts in the state-of-the-art web technologies, and are passionate about the cause of global online basic education. At the end of this project, we hope to have long term engagement with the selected developer(s) for our future website design and development needs.

Here are some preliminary guidelines on the MOVA Sphere website front end framework as envisioned by us so far. Please note that we would very much encourage creative ideas and mock-ups from the developers.

1. Current platform: Our website prototype back-end uses Drupal CMS (we plan to continue using Drupal CMS) and at the moment, a toy front-end is based on the Drupal Lattice platform for its simplicity, clean UI and mobile device friendliness. The web developer / designer can choose any Drupal front end as a starting point or come up with a new Drupal template that meets our requirements below. Prior experience and expertise on Drupal would be great.

2. Audience profile: While the primary audience for the website is expected to be young kids (6-10 years) not very familiar with English, the secondary audience also includes adults interested in basic English language skills. So the overall goal is to have simple, uncluttered / clean, elegant and lightweight (think loading time as well as mobile device friendliness) interface that is extremely intuitive and easy to navigate, is artistic and aesthetically appealing to a wide audience (especially the non-native English speaking populations). The most important point is that our target audience should feel welcome with the clean, crisp look and easy, user-centric navigation, and should in no case feel overwhelmed (say with too much text or clutter on the front page).

3. Front page: Here is a currently envisioned preliminary sketch of the website front page (very much open for refinement and improvements)
a. The top “menu bar” part of the landing page will have our organization name and logo along with (or above) the top menu bar with the following links and sub-links
i. “Learn” link with sub-menu of all our content sections (World learning, Basic sentence learning, Classic short stories, Picture Dictionary)
ii. “About” links with information about us (sub-menu entries: About MOVA Sphere, Team, Supporters, Contributors)
iii. “Contribute” link with sub-menu entries Donate, Volunteer
iv. Menu entries towards the right side: “Login / sign up” followed by
v. “Search” with space to enter the search phrase
b. The middle “main page content” part of the page is where we would have entry points to our main content categories. The portion is envisioned to be graphical, with big blocks (images) as links to our content categories. The current categories (to start with) include 1. Word learning, 2. Basic sentence learning, and 3. Classic stories. We welcome creative ideas to represent these content categories in an appealing and elegant way (for example, these content categories could be portrayed as closed double doors that lead to the pages with the content. We would like to have placeholders for appropriate image links to different content categories – we should be able to put appropriate images or change them as we come up with new ideas that would work best with our target audience). The categories would change and grow as our content evolves, hence the core idea is to build a flexible framework that readily allows for expansion as well as customization.
c. The bottom menu / links bar portion of the landing page will have a list of links that are not included at the top. Examples include (with flexibility needed to add more when needed)
i. “Help”: this leads to a new page with FAQ, How to use
ii. “Contact us” link to a web contact form page
iii. “For Teachers” link to a page with information such as how to use, tips, pilot programs,
iv. “Volunteer” link to page with links such as Donate, Volunteer
v. “Contributors” that would link to a page with information about our Artists, Teachers, Writers, Developers etc.
vi. “Jobs” would link to a jobs page
vii. “Blog” would lead to our blog page
viii. “User stories” link to pages with feedback that we obtain from the users about how the content has helped them,
ix. Web 2.0 placeholders for social media (to be added later)

d. The footer of the website should include text “2013 MOVA Sphere, All rights reserved.”

4. The middle block of the front page is the largest in screen real estate and perhaps the most challenging part that requires much creativity and thought on the UI/UX design aspect – the content pages pointed to by the section links on the middle portion of the front page are also being designed.

5. Color preference is towards soft, elegant (think grays, whites, light blues, other light colors) web safe colors. No harsh (too bright, garish) colors.

6. Fonts preference Nice, clean looking fonts (Arial alright) compatible across browsers.

7. Portability and robustness of the front page layout for different platforms should be carefully considered. Although our first launch target platform is PC (where cross browser compatibility is important), this would very soon be followed by mobile devices such as tablets and smartphones given their prevalence across the globe. This mobile friendly design or easy portability to mobile platforms with little work requirement should be considered as a design requirement.

8. Front page as a framework for the complete website: Note that the top and the bottom portions of the front page are envisioned be used as a common template / frame across all the pages of our website – the middle portion would be used to show our content on the other pages of our website.

9. UX: For the UI/UX design, it is critical to keep in mind key qualities such as ease of use, simplicity, elegance and artistic appeal. Some specific points to keep in mind: (1) the major portion of the target audience would be new to English and (2) young children are expected to be the primary audience but we want the website to appeal to adults interested in learning as well, and (3) we need the website to work even with relatively slow Internet speeds (for underdeveloped / developing regions especially), should always be kept in mind. HTML5 compliance ideas are encouraged.

10. Strictly not desired: Typical corporate feel seen in many webpages, blocky graphics, dull and uninviting overall look with no personality, Flash type effects, harsh colors.

11. Creativity and imagination necessary: We would like to reiterate that the designer/developer has complete freedom to re-imagine the front page considering the above requirements and get back with ideas for an inspiring layout that presents the content outlined above in an intuitive format, carefully considering our target audience.

A note: As a rule, we will always make sure that our developers and artists get proper credit for their work and are recognized and acknowledged by everyone visiting our website.

Expected deliverables:
Website design psd files AND coded webpage / Drupal template: the corresponding source code and all the required libraries, images etc would be required with minimal documentation / pointers on how to make changes and customizations.

Interested developers are encouraged to first send us preliminary prototype Design for the front page to get feedback on whether their approach and style is in line with our needs and preferences. We will suggest the developers to proceed further if the team thinks there is some potential for a match (of course, the final determination would be from the pool of shortlisted submissions) – otherwise, in case the team does not see potential for a match with our needs or if we have already received multiple submissions that are comparatively more closely aligned with our vision for the website, we'd prefer to be respectful of the developers’ time and effort by requesting them not to proceed further.

Please consider this effort as your contribution to an important social cause of global and accessible online education and not a commercial enterprise (our passion for making a positive impact is what is driving the MOVA Sphere nonprofit team to undertake this initiative!). We would like to invite you to join us in this effort!
Updates

Project Deadline Extended
Reason: Due to requests from interested designers, we are extending the deadline. Looking forward to receiving many other creative designs!

Target Market(s)

Please see the project brief.

Industry/Entity Type

Real Estate

Requirements
Nice to have
• Please see the project brief.
Should not have

```html
<!DOCTYPE html>
<html lang="en">
<head>
<meta charset="utf-8">
<title>MOVA Sphere – English learning for everyone</title>
<link href="https://fonts.googleapis.com/css2?family=Ubuntu:wght@400;500;700&display=swap" rel="stylesheet">
<style>
:root{
  --blue:#1ea3d8;
  --btn-top:#34bdf0;
  --btn-bottom:#1493cf;
  --ink:#4a4a4a;
  --card:rgba(10,10,10,.82);
  --card-title:#2cb3e8;
  --card-arrow:#1d6f90;
  --panel:#3c99ba;
  --footer:#3a90ae;
  --footer-bar:#2f7e9a;
  --coral:#e05757;
  --teal:#4b8fa1;
  --amber:#c8692c;
  --hero-top:#5f7f3c;
  --hero-bottom:#7d9c4f;
  --band-top:#ffffff;
  --band-bottom:#ececec;
}
*{margin:0;padding:0;box-sizing:border-box}
html,body{width:958px;height:1200px;overflow:hidden;background:#fff}
body{font-family:"Ubuntu",Arial,sans-serif;color:var(--ink)}
.page{position:relative;width:958px;height:1200px;overflow:hidden}
.abs{position:absolute}

/* header */
.brand{left:144px;top:20px;font-size:25px;font-weight:500;color:#5b5b5b;letter-spacing:-.3px}
.nav a{position:absolute;top:31px;font-size:8px;font-weight:500;color:#444;text-decoration:none}
.search{left:530px;top:25px;width:148px;height:20px;background:#ececec;border:1px solid #dcdcdc;font-size:7px;color:#999;padding:6px 8px}
.search svg{position:absolute;right:6px;top:4px}
.btn{display:flex;align-items:center;justify-content:center;color:#fff;font-size:7px;font-weight:500;background:linear-gradient(var(--btn-top),var(--btn-bottom));border-bottom:1px solid #0f6e9e;text-decoration:none}

/* hero */
.hero{left:0;top:67px;width:958px;height:417px;background:linear-gradient(180deg,var(--hero-top),var(--hero-bottom))}
.slide-arrow{width:50px;height:50px;border-radius:50%;display:flex;align-items:center;justify-content:center}
.slide-arrow.prev{left:80px;top:250px;background:rgba(200,210,215,.5)}
.slide-arrow.next{left:832px;top:250px;background:rgba(0,0,0,.12);border:1px solid rgba(255,255,255,.12)}
.category{top:409px;width:222px;height:69px;background:var(--card);color:#fff}
.category h3{position:absolute;left:15px;top:14px;font-size:12.5px;font-weight:500;color:var(--card-title)}
.category p{position:absolute;left:15px;top:38px;width:150px;font-size:7px;line-height:12px}
.category .go{position:absolute;right:0;bottom:0;width:45px;height:42px;background:var(--card-arrow);display:flex;align-items:center;justify-content:center}

/* mission band */
.band{left:0;top:484px;width:958px;height:84px;background:linear-gradient(var(--band-top),var(--band-bottom))}
.band h2{position:absolute;left:144px;top:14px;font-size:16px;font-weight:400;color:var(--blue)}
.band p{position:absolute;left:144px;top:38px;width:525px;font-size:8.3px;line-height:15px;color:#444}
.join{left:698px;top:510px;width:116px;height:32px;font-size:8.5px;font-weight:400;border-radius:2px}

/* welcome */
.section-title{left:144px;top:585px;font-size:16px;font-weight:400;color:var(--blue)}
.welcome-photo{left:144px;top:614px;width:185px;height:103px;background:linear-gradient(135deg,#d9a596,#eee4e0)}
.welcome-text{left:346px;top:617px;width:172px;font-size:7px;line-height:12.4px;color:#666}
.learn-photo{left:541px;top:594px;width:137px;height:123px;background:linear-gradient(135deg,#6e6f52,#4a4a48)}
.learn-panel{left:678px;top:594px;width:136px;height:123px;background:var(--panel);color:#fff;padding:11px 15px}
.learn-panel h3{font-size:12px;font-weight:500}
.learn-panel .lead{font-size:6.8px;margin-top:5px}
.learn-panel ul{list-style:none;margin-top:7px}
.learn-panel li{font-size:5.8px;line-height:12.3px}
.learn-panel li::before{content:"›";margin-right:4px}
.outline-btn{left:751px;top:692px;width:53px;height:15px;border:1px solid #fff;color:#fff;font-size:6.8px;display:flex;align-items:center;justify-content:center}

/* roles */
.pager{top:754px;width:13px;height:12px;background:#79d0f0;display:flex;align-items:center;justify-content:center}
.role{top:756px;width:232px;text-align:center}
.role .circle{width:92px;height:92px;border-radius:50%;margin:0 auto;display:flex;align-items:center;justify-content:center}
.role h3{margin-top:17px;font-size:13.5px;font-weight:400;color:var(--blue)}
.role p{margin:8px auto 0;width:200px;font-size:7.3px;line-height:13.6px;color:#777}
.role .btn{width:63px;height:18px;margin:9px auto 0;font-size:6.2px}

/* footer */
.footer{left:0;top:990px;width:958px;height:182px;background:var(--footer);color:#fff}
.footer h4{position:absolute;font-size:8px;font-weight:500}
.footer ul{position:absolute;list-style:none}
.footer li{font-size:6.2px;line-height:15.2px}
.email{left:433px;top:1104px;width:161px;height:16px;background:#2f7c99;border-bottom:1px solid #5aa9c6;font-size:6.2px;padding:5px 8px;color:#fff}
.send{left:543px;top:1125px;width:51px;height:16px;background:#5b5f63;font-size:6.8px;display:flex;align-items:center;justify-content:center;color:#fff}
.social{left:678px;display:flex;align-items:center;font-size:6.8px;color:#fff}
.social i{width:20px;height:20px;border-radius:50%;background:#2a6c8c;margin-right:5px;display:block}
.legal{left:0;top:1172px;width:958px;height:28px;background:var(--footer-bar);color:#fff;font-size:6.2px;padding:10px 0 0 146px}
</style>
</head>
<body>
<div class="page">

  <header>
    <div class="abs brand">MOVA Sphere</div>
    <nav class="nav">
      <a style="left:338px" href="#">LEARN</a>
      <a style="left:400px" href="#">ABOUT</a>
      <a style="left:462px" href="#">CONTRIBUTE</a>
    </nav>
    <div class="abs search">SEARCH :
      <svg width="12" height="12" viewBox="0 0 12 12"><circle cx="4.5" cy="4.5" r="3.3" fill="none" stroke="#aaa" stroke-width="1.3"/><line x1="7" y1="7" x2="11" y2="11" stroke="#aaa" stroke-width="1.8"/></svg>
    </div>
    <a class="abs btn" style="left:687px;top:25px;width:59px;height:20px" href="#">LOGIN</a>
    <a class="abs btn" style="left:754px;top:25px;width:60px;height:20px" href="#">SIGNUP</a>
  </header>

  <section>
    <div class="abs hero" role="img" aria-label="Hero photo: a group of students studying together outdoors on the grass"></div>
    <div class="abs slide-arrow prev"><svg width="12" height="20" viewBox="0 0 12 20"><polyline points="10,1 2,10 10,19" fill="none" stroke="#fff" stroke-width="1.2" stroke-dasharray="2 1.5"/></svg></div>
    <div class="abs slide-arrow next"><svg width="12" height="20" viewBox="0 0 12 20"><polyline points="2,1 10,10 2,19" fill="none" stroke="#ddd" stroke-width="1.2" stroke-dasharray="2 1.5"/></svg></div>

    <article class="abs category" style="left:144px">
      <h3>WORD LEARNING</h3>
      <p>Lorem Ipsum is simply dummy text of the printing and typesetting industry.</p>
      <a class="go" href="#"><svg width="10" height="14" viewBox="0 0 10 14"><polyline points="2,1 8,7 2,13" fill="none" stroke="#fff" stroke-width="2.4"/></svg></a>
    </article>
    <article class="abs category" style="left:368px">
      <h3>BASIC SENTENCE LEARNING</h3>
      <p>Lorem Ipsum is simply dummy text of the printing and typesetting industry.</p>
      <a class="go" href="#"><svg width="10" height="14" viewBox="0 0 10 14"><polyline points="2,1 8,7 2,13" fill="none" stroke="#fff" stroke-width="2.4"/></svg></a>
    </article>
    <article class="abs category" style="left:592px">
      <h3>CLASSIC STORIES</h3>
      <p>Lorem Ipsum is simply dummy text of the printing and typesetting industry.</p>
      <a class="go" href="#"><svg width="10" height="14" viewBox="0 0 10 14"><polyline points="2,1 8,7 2,13" fill="none" stroke="#fff" stroke-width="2.4"/></svg></a>
    </article>
  </section>

  <section class="abs band">
    <h2>We are non profit english learning online platform.</h2>
    <p>Lorem Ipsum is simply dummy text of the printing and typesetting industry. Lorem Ipsum has been the industry's standard dummy text ever since the 1500s</p>
  </section>
  <a class="abs btn join" href="#">JOIN FOR LEARNING</a>

  <section>
    <h2 class="abs section-title">Welcome to MOVA Sphere</h2>
    <div class="abs welcome-photo" role="img" aria-label="Photo: a young learner working on a laptop"></div>
    <p class="abs welcome-text">Lorem Ipsum is simply dummy text of the printing and typesetting industry. Lorem Ipsum has been the industry's standard dummy text ever since the 1500s, when an unknown printer took a galley of type and scrambled it to make a type specimen book. It has survived not only five centuries, but also the leap into electronic typesetting, remaining essentially unchanged.</p>
    <div class="abs learn-photo" role="img" aria-label="Photo: a student with a headset in a computer classroom"></div>
    <div class="abs learn-panel">
      <h3>LEARN</h3>
      <div class="lead">Lorem Ipsum is simply dummy...</div>
      <ul>
        <li>WORD LEARNING</li>
        <li>BASIC SENTENCE LEARNING</li>
        <li>CLASSIC SHORT STORIES</li>
        <li>PICTURE DICTIONARY</li>
      </ul>
    </div>
    <a class="abs outline-btn" href="#">READ MORE</a>
  </section>

  <section>
    <div class="abs pager" style="left:783px"><svg width="5" height="7" viewBox="0 0 5 7"><polyline points="4,1 1,3.5 4,6" fill="none" stroke="#fff"/></svg></div>
    <div class="abs pager" style="left:800px"><svg width="5" height="7" viewBox="0 0 5 7"><polyline points="1,1 4,3.5 1,6" fill="none" stroke="#fff"/></svg></div>

    <article class="abs role" style="left:134px">
      <div class="circle" style="background:var(--coral)">
        <svg width="40" height="36" viewBox="0 0 40 36"><circle cx="20" cy="7" r="5" fill="#fff"/><path d="M4 14 L20 22 L36 14 L36 28 L20 35 L4 28 Z" fill="#fff"/><path d="M20 22 L20 35" stroke="#e05757" stroke-width="1.5"/></svg>
      </div>
      <h3>For teachers</h3>
      <p>Lorem Ipsum is simply dummy text of the printing and typesetting industry. Lorem Ipsum has been the industry's standard dummy text ever since the 1500s...</p>
      <a class="btn" href="#">READ MORE</a>
    </article>
    <article class="abs role" style="left:366px">
      <div class="circle" style="background:var(--teal)">
        <svg width="42" height="42" viewBox="0 0 42 42"><path d="M4 18 H11 V38 H4 Z M14 19 L21 5 C24 4 26 6 25 10 L23 16 H35 C38 16 39 19 37 21 C39 23 38 25 36 26 C38 28 37 30 35 31 C36 33 35 36 32 36 H14 Z" fill="none" stroke="#fff" stroke-width="2.2" stroke-linejoin="round"/></svg>
      </div>
      <h3>Volunteer</h3>
      <p>Lorem Ipsum is simply dummy text of the printing and typesetting industry. Lorem Ipsum has been the industry's standard dummy text ever since the 1500s...</p>
      <a class="btn" href="#">READ MORE</a>
    </article>
    <article class="abs role" style="left:599px">
      <div class="circle" style="background:var(--amber)">
        <svg width="52" height="40" viewBox="0 0 52 40"><ellipse cx="21" cy="15" rx="18" ry="12" fill="#fff"/><path d="M10 24 L6 33 L17 26 Z" fill="#fff"/><ellipse cx="34" cy="24" rx="14" ry="9" fill="#fff" stroke="#c8692c" stroke-width="2"/><path d="M40 31 L46 38 L44 29 Z" fill="#fff"/></svg>
      </div>
      <h3>Contributors</h3>
      <p>Lorem Ipsum is simply dummy text of the printing and typesetting industry. Lorem Ipsum has been the industry's standard dummy text ever since the 1500s...</p>
      <a class="btn" href="#">READ MORE</a>
    </article>
  </section>

  <footer class="abs footer">
    <h4 style="left:144px;top:14px">WELCOME</h4>
    <ul style="left:145px;top:29px">
      <li>HELP</li><li>CONTACT US</li><li>FOR TEACHERS</li><li>VOLUNTEER</li><li>CONTRIBUTORS</li><li>JOBS</li><li>BLOG</li><li>USER STORIES</li>
    </ul>
    <h4 style="left:274px;top:14px">LEARN</h4>
    <ul style="left:275px;top:29px">
      <li>WORD LEARNING</li><li>BASIC SENTENCE LEARNING</li><li>CLASSIC SHORT STORIES</li><li>PICTURE DICTIONARY</li>
    </ul>
    <h4 style="left:274px;top:96px">ABOUT</h4>
    <ul style="left:275px;top:111px">
      <li>ABOUT MOVA SPHERE</li><li>TEAM</li><li>SUPPORTERS</li><li>CONTRIBUTORS</li>
    </ul>
    <h4 style="left:432px;top:21px">CONTRIBUTE</h4>
    <ul style="left:433px;top:36px">
      <li>DONATE</li><li>VOLUNTEER</li>
    </ul>
    <h4 style="left:432px;top:80px">NEWSLETTER SIGNUP</h4>
    <ul style="left:433px;top:92px"><li>GET OUR RECENT UPDATES THROUGH YOUR EMAIL :</li></ul>
  </footer>
  <div class="abs email">ENTER YOUR EMAIL D :</div>
  <div class="abs send">SEND</div>
  <div class="abs social" style="top:1009px"><i></i>: CIRCLEBOOK</div>
  <div class="abs social" style="top:1036px"><i style="background:#4fb6e0"></i>: CHIRPLINE</div>
  <div class="abs social" style="top:1063px"><i></i>: WORKLINK</div>

  <div class="abs legal">COPYRIGHT 2013 MOVA SPHERE. ALL RIGHTS RESERVED.</div>
</div>
</body>
</html>
```